Design some Business Cards for Ski Trainer

1. A namecard with orange and white major color for a female Ski instructor
2. Prefer using more icons
3. Please use the same logo of http://www.frostpeakcoaching.example/ ( as seen in attached file, but you may need to reconstruct the logo again)
4. text detail for the content is attached
5. Please DO NOT use traditional fonts
6. We would like to use the font "Showcard Gothic " for the company name "Frost & Peak Coaching"

```html
<!DOCTYPE html>
<html lang="en">
<head>
<meta charset="utf-8">
<title>Frost &amp; Peak Coaching – Business Cards</title>
<link rel="stylesheet" href="https://fonts.googleapis.com/css2?family=Lato:wght@400;700;900&display=swap">
<style>
  :root {
    --stage: #2b2b2d;
    --orange: #f0a020;
    --orange-deep: #e08c12;
    --ink: #1c1c1c;
    --white: #ffffff;
    --sky: #4f7397;
    --snow: #e9eef3;
    --slate: #8a96a3;
    --icon-bg: #2a2a2a;
  }
  * { margin: 0; padding: 0; box-sizing: border-box; }
  html, body { width: 1200px; height: 891px; overflow: hidden; }
  body {
    background: var(--stage);
    font-family: "Lato", Arial, sans-serif;
    position: relative;
  }
  .card {
    position: absolute;
    width: 520px;
    height: 300px;
    border-radius: 22px;
    overflow: hidden;
    background: var(--white);
    box-shadow: 0 10px 30px rgba(0,0,0,.45);
  }
  .card--front { left: 90px; top: 140px; }
  .card--back  { left: 590px; top: 450px; }

  .photo {
    position: absolute;
    inset: 0;
  }
  .card--front .photo {
    background: linear-gradient(160deg, #1f2a38 0%, #6f8397 30%, #d9e0e7 60%, #f4f6f8 100%);
  }
  .card--back .photo {
    background: linear-gradient(150deg, var(--sky) 0%, #9db4c9 30%, var(--snow) 55%, #f6f8fa 100%);
  }
  .shapes { position: absolute; inset: 0; }

  .figure-slot {
    position: absolute;
    background: rgba(80,90,100,.35);
    border-radius: 6px;
  }

  .site-url {
    position: absolute;
    top: 18px; right: 26px;
    color: var(--white);
    font-size: 11px;
    letter-spacing: .06em;
    font-weight: 700;
  }

  .brand {
    position: absolute;
    display: flex;
    align-items: center;
    gap: 8px;
    font-family: "Lato", Arial, sans-serif;
    font-weight: 900;
    font-size: 20px;
    letter-spacing: .03em;
  }
  .brand-dot {
    width: 18px; height: 18px;
    border-radius: 50%;
  }
  .card--front .brand { left: 300px; top: 150px; color: var(--orange); }
  .card--front .brand-dot { background: var(--ink); }
  .card--back .brand { left: 28px; top: 150px; color: var(--ink); }
  .card--back .brand-dot { background: var(--white); }

  .identity {
    position: absolute;
    top: 16px; right: 26px;
    text-align: right;
  }
  .identity-name {
    color: var(--orange);
    font-size: 20px;
    font-weight: 700;
  }
  .identity-role {
    color: var(--orange-deep);
    font-size: 11px;
    margin-top: 2px;
  }

  .contact-list {
    position: absolute;
    left: 22px; top: 188px;
    list-style: none;
  }
  .contact-item {
    display: flex;
    align-items: center;
    gap: 10px;
    height: 24px;
    color: var(--white);
    font-size: 11.5px;
    letter-spacing: .04em;
  }
  .contact-icon {
    width: 18px; height: 18px;
    border-radius: 3px;
    background: var(--icon-bg);
    display: flex; align-items: center; justify-content: center;
  }
</style>
</head>
<body>

  <section class="card card--front" aria-label="Card front">
    <div class="photo" role="img" aria-label="Photo of a skier descending a snowy mountain slope"></div>
    <svg class="shapes" viewBox="0 0 520 300" aria-hidden="true">
      <path d="M0 0 H520 V34 H360 C320 34 300 60 280 90 L150 300 H0 Z" fill="#1d2530" opacity="0"/>
      <path d="M0 0 H520 V36 H370 Q330 36 300 80 L160 300 H0 Z" fill="none"/>
      <path d="M370 0 H520 V300 H170 L300 70 Q330 30 370 30 Z" fill="#ffffff"/>
      <path d="M0 0 H520 V30 H370 Q330 30 300 70 L295 78 Q325 10 380 0 Z" fill="#1f2a38"/>
    </svg>
    <div class="figure-slot" role="img" aria-label="Silhouettes of skiers and snowboarders" style="left:250px; top:60px; width:200px; height:80px;"></div>
    <p class="site-url">WWW.FROSTPEAKCOACHING.EXAMPLE</p>
    <div class="brand"><span class="brand-dot"></span>FROST &amp; PEAK</div>
  </section>

  <section class="card card--back" aria-label="Card back">
    <div class="photo" role="img" aria-label="Photo of a skier in red carving down a bright snow slope"></div>
    <svg class="shapes" viewBox="0 0 520 300" aria-hidden="true">
      <path d="M0 70 Q20 64 40 74 L440 300 H0 Z" fill="var(--orange)"/>
    </svg>
    <div class="figure-slot" role="img" aria-label="Faded skier silhouette on the orange band" style="left:200px; top:150px; width:110px; height:70px; background:rgba(255,255,255,.22);"></div>
    <div class="identity">
      <p class="identity-name">Marina Holt</p>
      <p class="identity-role">Ski Instructor &amp; Snowboard Coach</p>
    </div>
    <div class="brand"><span class="brand-dot"></span>FROST &amp; PEAK</div>
    <ul class="contact-list">
      <li class="contact-item">
        <span class="contact-icon">
          <svg width="12" height="12" viewBox="0 0 24 24"><path d="M6.6 10.8a15 15 0 0 0 6.6 6.6l2.2-2.2a1 1 0 0 1 1-.25 11.4 11.4 0 0 0 3.6.57 1 1 0 0 1 1 1V20a1 1 0 0 1-1 1A17 17 0 0 1 3 4a1 1 0 0 1 1-1h3.5a1 1 0 0 1 1 1c0 1.25.2 2.45.57 3.57a1 1 0 0 1-.25 1z" fill="#fff"/></svg>
        </span>(852) 5550 0142
      </li>
      <li class="contact-item">
        <span class="contact-icon">
          <svg width="12" height="12" viewBox="0 0 24 24"><rect x="2" y="5" width="20" height="14" rx="1" fill="none" stroke="#fff" stroke-width="2"/><path d="M2 6l10 7 10-7" fill="none" stroke="#fff" stroke-width="2"/></svg>
        </span>MARINAHOLT.SKI@MAILBOX.EXAMPLE
      </li>
      <li class="contact-item">
        <span class="contact-icon">
          <svg width="12" height="12" viewBox="0 0 24 24"><circle cx="12" cy="12" r="9" fill="none" stroke="#fff" stroke-width="2"/><path d="M3 12h18M12 3c3 3 3 15 0 18M12 3c-3 3-3 15 0 18" fill="none" stroke="#fff" stroke-width="1.6"/></svg>
        </span>WWW.FROSTPEAKCOACHING.EXAMPLE
      </li>
      <li class="contact-item">
        <span class="contact-icon"></span>FROST &amp; PEAK COACHING
      </li>
    </ul>
  </section>

</body>
</html>
```